Business Card Design

Electronic Security
Alarm Systems
CCTV
Electronic Access Control
Security System Integration

Industry/Entity Type

Business

Contact Information for Business Card

Declan Whitfield
PO Box 862
Carrowbrook Qld 4179
Phone 07 38265014
Mob 0428615937

```html
<!DOCTYPE html>
<html lang="en">
<head>
<meta charset="utf-8">
<title>Korvel Business Card</title>
<link rel="stylesheet" href="https://fonts.googleapis.com/css2?family=Source+Sans+3:wght@400;600;700&display=swap">
<style>
  :root {
    --backdrop: #1f5670;
    --card: #ffffff;
    --ink: #222222;
    --muted: #555555;
    --teal: #1b8fa8;
    --brand: #1f9ac9;
    --orange: #f2994a;
    --rule: #333333;
  }
  * { margin: 0; padding: 0; box-sizing: border-box; }
  html, body { width: 1200px; height: 385px; overflow: hidden; }
  body {
    background: var(--backdrop);
    font-family: "Source Sans 3", Arial, sans-serif;
    color: var(--ink);
    position: relative;
  }
  .card {
    position: absolute;
    top: 44px;
    width: 529px;
    height: 302px;
    background: var(--card);
    overflow: hidden;
    box-shadow: 0 4px 14px rgba(0,0,0,0.35);
  }
  .card--front { left: 49px; }
  .card--back { left: 626px; }

  .decor {
    position: absolute;
    top: 0;
    right: 0;
    border-radius: 0 0 0 60px;
  }
  .card--front .decor {
    width: 130px; height: 245px;
    background: linear-gradient(135deg, #b9c4cc 0%, #9fd3ee 40%, #fde6c8 70%, #cfd6dc 100%);
    opacity: 0.8;
  }
  .card--back .decor {
    width: 145px; height: 294px;
    background: linear-gradient(135deg, #dfe4e8 0%, #cfe9f6 40%, #fdf0de 70%, #e4e8eb 100%);
    opacity: 0.8;
  }

  .brand {
    position: absolute;
    display: flex;
    flex-direction: column;
    align-items: center;
  }
  .brand__mark {
    border-radius: 50%;
    background: var(--brand);
  }
  .brand__name {
    font-weight: 600;
    color: var(--brand);
    letter-spacing: 1px;
  }
  .card--front .brand { left: 20px; top: 40px; width: 150px; }
  .card--front .brand__mark { width: 62px; height: 62px; margin-bottom: 14px; }
  .card--front .brand__name { font-size: 30px; }

  .card--back .brand { left: 140px; top: 50px; width: 230px; }
  .card--back .brand__mark { width: 100px; height: 100px; margin-bottom: 20px; }
  .card--back .brand__name { font-size: 48px; }

  .divider {
    position: absolute;
    left: 235px; top: 30px;
    width: 2px; height: 143px;
    background: var(--rule);
  }
  .services {
    position: absolute;
    left: 258px; top: 27px;
    list-style: none;
    font-size: 13px;
  }
  .services li {
    display: flex;
    align-items: center;
    height: 31.5px;
  }
  .services li::before {
    content: "";
    width: 7px; height: 7px;
    background: var(--brand);
    margin-right: 10px;
  }

  .person { position: absolute; left: 29px; top: 230px; }
  .person__name { font-size: 17px; font-weight: 700; color: var(--teal); }
  .person__title { font-size: 11px; color: var(--muted); margin-top: 6px; }

  .contact { position: absolute; left: 258px; top: 229px; font-size: 12.5px; }
  .contact__phones { margin-top: 11px; }
  .contact__label { font-weight: 700; }
  .contact__sep { margin: 0 9px; color: var(--muted); }

  .stripe {
    position: absolute; left: 0; right: 0; bottom: 0;
    height: 9px;
    background: var(--teal);
    border-top: 2px solid var(--orange);
  }
</style>
</head>
<body>
  <section class="card card--front">
    <div class="decor" role="img" aria-label="Faint large brand symbol decoration"></div>
    <div class="brand">
      <span class="brand__mark"></span>
      <span class="brand__name">KORVEL</span>
    </div>
    <span class="divider"></span>
    <ul class="services">
      <li>Electronic Security</li>
      <li>Alarm Systems</li>
      <li>CCTV</li>
      <li>Electronic Access Control</li>
      <li>Security System Integration</li>
    </ul>
    <div class="person">
      <p class="person__name">Declan Whitfield</p>
      <p class="person__title">Title Goes Here</p>
    </div>
    <div class="contact">
      <p>PO Box 862 Carrowbrook Qld 4179</p>
      <p class="contact__phones"><span class="contact__label">Ph:</span> 07 38265014<span class="contact__sep">|</span><span class="contact__label">Mob:</span> 0428615937</p>
    </div>
    <div class="stripe"></div>
  </section>

  <section class="card card--back">
    <div class="decor" role="img" aria-label="Faint large brand symbol decoration"></div>
    <div class="brand">
      <span class="brand__mark"></span>
      <span class="brand__name">KORVEL</span>
    </div>
  </section>
</body>
</html>
```